Computer consultant website

Vexlo Software is a newly started computer consulting company. It's a small one-man company that provides mostly Android applications but also websites in collaboration with designers. I'm running this company on the side of full time university studies.

I'm in need of a website which will function as:
Primarily - I'll direct potential clients to the page so they can read about the company, what i offer and past work.
Secondarily - Making my company visible through the web and maybe getting new clients.

The final design should look modern, clean and professional.

Pages that will be in the final website are (Note that it's not the exact titles as the page will not be in english):
* About
* Services (what Vexlo offers)
* Portfolio/work
* Short news (like PlanHives "News and press")
* Contact.

Inspiration
http://www.planhive.example/design/87836
http://www.brambleorb.example/
http://www.planhive.example/design/845881
http://www.planhive.example/design/1369424 - Lighter design, however a bit cluttered.

No programming code is needed delivered at all. Focus on designing rather then coding.

If you have any questions, do not hesitate to send me a message.

Target Market(s)

Non-technical entrepreneurs and small companies.

Industry/Entity Type

University

Requirements
Must have
• Must have my company logo (see attachment).

Must in any way use both colors from my logo.

A way to logically rearrange content to fit smaller screens. I will implement this design so that it can be pleasantly viewed on mobile devices. You don't necessarily need to provide exactly how the design would look on mobile devices.

I need the following types of page designs:
* Landing page
* Content page
* Portfolio/work (with accompanying inside/clicked) page

Landing/start page must in any way include at least the information:
* Shorter version of "About Vexlo"
* At least 1 most recent portfolio/work entry
* At least 1 most recent news entry
* Services that Vexlo offers.
Nice to have
Should not have
• Testimonials or newsletter.

```html
<!DOCTYPE html>
<html lang="en">
<head>
<meta charset="utf-8">
<title>Vexlo Software</title>
<link rel="stylesheet" href="https://fonts.googleapis.com/css2?family=Cabin:wght@400;500&family=Open+Sans:wght@400;600&family=Pathway+Gothic+One&display=swap">
<style>
:root{
  --blue:#1c6cb4;
  --blue-bright:#3a7fd6;
  --link:#2a8fd8;
  --ink:#2b2b2b;
  --text:#6d6d6d;
  --muted:#8a8a8a;
  --sidebar:#ebebeb;
  --service-bg:#d7ebf1;
  --line:#cfd6d9;
  --footer:#000;
  --orange:#f39a1b;
}
*{margin:0;padding:0;box-sizing:border-box}
html,body{width:1179px;height:1200px;overflow:hidden;background:#fff}
body{font-family:"Open Sans",sans-serif;color:var(--text);position:relative}
.page{position:relative;width:1179px;height:1200px;overflow:hidden}
a{color:inherit;text-decoration:none}

/* header */
.header{position:absolute;left:0;top:0;width:1179px;height:100px;background:#fff;box-shadow:0 2px 4px rgba(0,0,0,.08);z-index:2}
.brand{position:absolute;left:138px;top:20px;display:flex;align-items:center;gap:14px}
.brand-mark{width:60px;height:60px;border-radius:50%;background:var(--blue-bright)}
.brand-name{font-family:"Cabin",sans-serif;font-weight:500;font-size:52px;color:var(--ink);letter-spacing:-1px;line-height:1}
.nav{position:absolute;right:136px;top:34px;display:flex;gap:18px;font-family:"Open Sans",sans-serif;font-weight:600;font-size:15px;color:#444}
.nav a{padding:7px 10px;border-radius:3px}
.nav a.active{background:var(--blue-bright);color:#fff}

/* hero */
.hero{position:absolute;left:0;top:100px;width:1179px;height:464px;background:linear-gradient(90deg,#8d8a86 0%,#c9c2b8 30%,#e6e3de 55%,#b6a89a 78%,#dcd8d2 100%)}
.hero-caption{position:absolute;left:0;top:483px;width:849px;height:81px;background:var(--blue);color:#fff;font-family:"Cabin",sans-serif;font-size:30px;line-height:32px;padding:8px 0 0 138px}
.slider-tab{position:absolute;left:849px;top:483px;width:193px;height:81px;background:#dcdcdc}
.slider-tab svg{position:absolute;left:0;top:0}

/* sidebar */
.sidebar{position:absolute;left:849px;top:564px;width:330px;height:582px;background:var(--sidebar)}
.side-title{font-family:"Pathway Gothic One",sans-serif;font-size:26px;color:var(--blue-bright);position:absolute;left:15px}
.contact-row{position:absolute;left:15px;width:178px;height:30px;border-bottom:1px solid #d6d6d6;display:flex;align-items:center;justify-content:space-between;font-size:13px}
.contact-row .val{color:#555}
.contact-row .val.link{color:var(--link)}
.news-item{position:absolute;left:15px;width:180px;display:flex;gap:9px}
.news-date{text-align:center;width:26px;font-family:"Cabin",sans-serif;color:#333}
.news-date b{display:block;font-weight:400;font-size:24px;line-height:24px}
.news-date span{font-size:12px;color:#777}
.news-body h4{font-weight:600;font-size:13px;color:#222;margin-bottom:4px}
.news-body p{font-size:11.5px;line-height:16px;color:#777}
.follow-row{position:absolute;left:15px;width:178px;height:40px;border-bottom:1px solid #d6d6d6;display:flex;align-items:center;gap:13px;font-size:12.5px;color:var(--link)}
.follow-row i{width:26px;height:26px;display:block}

/* main */
.welcome-title{position:absolute;left:138px;top:583px;font-family:"Pathway Gothic One",sans-serif;font-size:46px;color:var(--blue-bright);line-height:1}
.intro{position:absolute;left:138px;top:645px;width:410px;font-size:14px;line-height:21.3px;color:var(--text)}
.intro p+p{margin-top:21px}
.services{position:absolute;left:568px;top:594px;width:253px;height:342px;background:var(--service-bg);border-radius:4px;padding:13px 14px}
.services h3{font-family:"Pathway Gothic One",sans-serif;font-weight:400;font-size:25px;color:var(--blue-bright);margin-bottom:11px}
.services li{list-style:none;height:32px;border-bottom:1px dotted #aac3cc;display:flex;align-items:center;gap:8px;font-size:14px;color:#2f5d7e}
.services li:last-child{border-bottom:none}
.services li svg{flex:none}
.jobs-title{position:absolute;left:138px;top:966px;font-family:"Pathway Gothic One",sans-serif;font-size:25px;color:var(--blue-bright)}
.job{position:absolute;top:1012px;display:flex;gap:10px;width:220px}
.job-photo{width:96px;height:96px;background:#e9e9e9;padding:8px;flex:none}
.job-photo div{width:100%;height:100%}
.job h4{font-weight:600;font-size:13px;color:#222;margin:-2px 0 8px}
.job p{font-size:11.5px;line-height:16.5px;color:#777}

/* footer */
.footer{position:absolute;left:0;top:1146px;width:1179px;height:54px;background:var(--footer);color:#9a9a9a;font-size:14px}
.footer-nav{position:absolute;left:138px;top:18px;display:flex;gap:28px}
.copyright{position:absolute;right:137px;top:18px;color:#fff;font-size:13px}
</style>
</head>
<body>
<div class="page">

  <header class="header">
    <div class="brand"><span class="brand-mark"></span><span class="brand-name">Vexlo</span></div>
    <nav class="nav">
      <a class="active">ABOUT</a><a>SERVICES</a><a>PORTFOLIO/WORK</a><a>SHORT NEWS</a><a>CONTACT</a>
    </nav>
  </header>

  <div class="hero" role="img" aria-label="Photo of three smiling business people talking in an office"></div>
  <div class="hero-caption">Lorem Ipsum. Proin gravida nibh vel velit<br>auctor aliquet.</div>
  <div class="slider-tab">
    <svg width="193" height="100" viewBox="0 0 193 100">
      <circle cx="70" cy="39" r="5" fill="none" stroke="#a9a9a9"/>
      <circle cx="87" cy="39" r="5" fill="#a9a9a9"/>
      <circle cx="104" cy="39" r="5" fill="none" stroke="#a9a9a9"/>
      <circle cx="121" cy="39" r="5" fill="none" stroke="#a9a9a9"/>
    </svg>
  </div>

  <aside class="sidebar">
    <svg width="40" height="12" style="position:absolute;left:76px;top:0"><polygon points="0,0 40,0 20,12" fill="#dcdcdc"/></svg>
    <h3 class="side-title" style="top:20px">Contact Us</h3>
    <div class="contact-row" style="top:52px">
      <svg width="22" height="18" viewBox="0 0 22 18"><path d="M2 6c0-3 4-4 9-4s9 1 9 4v2h-5V6H7v2H2z" fill="var(--orange)"/><rect x="4" y="9" width="14" height="8" rx="1" fill="var(--orange)"/><circle cx="11" cy="13" r="2" fill="#fff"/></svg>
      <span class="val">555-014-2290</span>
    </div>
    <div class="contact-row" style="top:84px">
      <svg width="22" height="16" viewBox="0 0 22 16"><rect width="22" height="16" fill="var(--orange)"/><path d="M0 0l11 9 11-9" fill="none" stroke="#fff" stroke-width="1.5"/></svg>
      <span class="val link">info@vexlo.example</span>
    </div>

    <h3 class="side-title" style="top:128px">Latest News</h3>
    <div class="news-item" style="top:172px">
      <div class="news-date"><b>20</b><span>JAN</span></div>
      <div class="news-body"><h4>Lorem ipsum dolor sit.</h4><p>Maecenas sollicitudin lorem in orci element um nec semper.</p></div>
    </div>
    <div class="news-item" style="top:265px">
      <div class="news-date"><b>18</b><span>JAN</span></div>
      <div class="news-body"><h4>Lorem ipsum dolor sit.</h4><p>Maecenas sollicitudin lorem in orci element um nec semper.</p></div>
    </div>

    <h3 class="side-title" style="top:358px">Follow Us</h3>
    <div class="follow-row" style="top:393px"><i style="background:#3b5a98"></i>Connect on Friendnet</div>
    <div class="follow-row" style="top:433px"><i style="background:#3a8fc4"></i>Follow on Chirper</div>
    <div class="follow-row" style="top:473px"><i style="background:#4d9ec4"></i>Connect on Linkwork</div>
    <div class="follow-row" style="top:513px"><i style="background:#dd3f2e"></i>Connect on Circleplus</div>
  </aside>

  <h1 class="welcome-title">Welcome to Vexlo</h1>
  <div class="intro">
    <p>Lorem Ipsum. Proin gravida nibh vel velit auctor aliquet. Aenean sollicitudin, lorem quis bibendum auctor, nisi elit consequat ipsum, nec sagittis sem nibh id elit. Duis sed odio sit amet nibh vulputate cursus a sit amet mauris. Morbi accumsan ipsum velit. Nam nec tellus a odio tincidunt auctor a ornare odio. Sed non mauris vitae erat consequat auctor eu in elit. Class aptent taciti sociosqu ad litora torquent per</p>
    <p>conubia nostra, per inceptos himenaeos. Mauris in erat justo. Nullam ac urna eu felis dapibus condimentum sit amet a augue. Sed non neque elit. Sed ut imperdiet nisi. Proin condimentum fermentum nunc. Etiam pharetra, erat sed fermentum feugiat, velit mauris egestas quam, ut aliquam massa nisl quis neque. Suspendisse in orci enim.</p>
  </div>

  <section class="services">
    <h3>Our Services</h3>
    <ul>
      <li><svg width="7" height="8"><path d="M1 1l4 3-4 3" fill="none" stroke="#6a9bb3"/></svg>Suspendisse egestas dui ac</li>
      <li><svg width="7" height="8"><path d="M1 1l4 3-4 3" fill="none" stroke="#6a9bb3"/></svg>Proin id risus sed sem</li>
      <li><svg width="7" height="8"><path d="M1 1l4 3-4 3" fill="none" stroke="#6a9bb3"/></svg>Sed non lectus orci</li>
      <li><svg width="7" height="8"><path d="M1 1l4 3-4 3" fill="none" stroke="#6a9bb3"/></svg>Sed sit amet urna orci</li>
      <li><svg width="7" height="8"><path d="M1 1l4 3-4 3" fill="none" stroke="#6a9bb3"/></svg>Suspendisse egestas dui ac</li>
      <li><svg width="7" height="8"><path d="M1 1l4 3-4 3" fill="none" stroke="#6a9bb3"/></svg>Proin id risus sed sem</li>
      <li><svg width="7" height="8"><path d="M1 1l4 3-4 3" fill="none" stroke="#6a9bb3"/></svg>Sed non lectus orci</li>
      <li><svg width="7" height="8"><path d="M1 1l4 3-4 3" fill="none" stroke="#6a9bb3"/></svg>Sed sit amet urna orci</li>
    </ul>
  </section>

  <h3 class="jobs-title">Latest Job</h3>
  <div class="job" style="left:138px">
    <div class="job-photo"><div role="img" aria-label="Portrait photo of a woman" style="background:linear-gradient(#c9a27f,#3a3f4a)"></div></div>
    <div><h4>Lorem ipsum</h4><p>Maecenas sollicitudin lorem in orci element um nec semper.</p></div>
  </div>
  <div class="job" style="left:367px">
    <div class="job-photo"><div role="img" aria-label="Portrait photo of a man in a suit" style="background:linear-gradient(#b88c6c,#2f3440)"></div></div>
    <div><h4>Lorem ipsum</h4><p>Maecenas sollicitudin lorem in orci element um nec semper.</p></div>
  </div>
  <div class="job" style="left:597px">
    <div class="job-photo"><div role="img" aria-label="Portrait photo of a young man with glasses" style="background:linear-gradient(#e7e4e0,#b89a82)"></div></div>
    <div><h4>Lorem ipsum</h4><p>Maecenas sollicitudin lorem in orci element um nec semper.</p></div>
  </div>

  <footer class="footer">
    <nav class="footer-nav"><a>ABOUT</a><a>SERVICES</a><a>PORTFOLIO/WORK</a><a>SHORT NEWS</a><a>CONTACT</a></nav>
    <div class="copyright">© 2013 VEXLO. ALL RIGHTS RESERVED.</div>
  </footer>

</div>
</body>
</html>
```